Vértice Lunar Presentation

We already have a logo, and now we need a good presentation for our company. You can seach for us at : verticelunar.pt and see more about us. We work in adaptive reuse of buildings. You can ask anything you need to do a great job.

Industry/Entity Type

It Company

```html
<!DOCTYPE html>
<html lang="pt">
<head>
<meta charset="utf-8">
<title>Vértice Lunar — Presentation Template</title>
<link rel="stylesheet" href="https://fonts.googleapis.com/css2?family=Source+Sans+3:wght@400;600;700&family=Ubuntu:wght@400;500;700&display=swap">
<style>
  :root {
    --brand: #4364B0;
    --white: #FFFFFF;
    --sheet: #DCDCDC;
    --copy-grey: #6A6A6A;
    --rule: #CFCFCF;
    --ghost: #EEF1F8;
    --photo-warm-1: #c9b79c;
    --photo-warm-2: #6d5a47;
    --photo-cool-1: #3d5aa5;
    --photo-cool-2: #1c2a55;
  }
  * { box-sizing: border-box; margin: 0; padding: 0; }
  html, body { width: 1200px; height: 782px; overflow: hidden; }
  body {
    position: relative;
    background: var(--sheet);
    font-family: "Source Sans 3", "Source Sans Pro", sans-serif;
  }

  .slide {
    position: absolute;
    width: 367px;
    height: 206px;
    background: var(--white);
    overflow: hidden;
    box-shadow: 0 1px 2px rgba(0,0,0,0.12);
  }
  .col-1 { left: 26px; } .col-2 { left: 419px; } .col-3 { left: 811px; }
  .row-1 { top: 34px; } .row-2 { top: 263px; } .row-3 { top: 496px; }

  /* Cover */
  .cover-mark { position: absolute; left: 62px; top: 93px; width: 86px; text-align: center; }
  .cover-mark .dot { display: block; width: 12px; height: 12px; border-radius: 50%; background: var(--brand); margin: 0 auto 4px; }
  .cover-mark .name { font-family: "Ubuntu", sans-serif; font-weight: 500; font-size: 12px; color: var(--brand); white-space: nowrap; }
  .cover-divider { position: absolute; left: 158px; top: 86px; width: 1px; height: 42px; background: var(--rule); }
  .cover-title { position: absolute; left: 170px; top: 94px; font-family: "Ubuntu", sans-serif; font-weight: 700; font-size: 15px; letter-spacing: 0.6px; color: var(--brand); }
  .cover-subtitle { position: absolute; left: 171px; top: 113px; font-size: 6px; letter-spacing: 0.6px; color: #AFAFAF; }
  .cover-footer { position: absolute; left: 0; bottom: 0; width: 100%; height: 9px; background: var(--brand); display: flex; justify-content: space-between; align-items: center; padding: 0 5px; font-size: 3px; font-weight: 700; letter-spacing: 0.2px; color: var(--white); }

  /* Full-width header bar */
  .top-bar { position: absolute; left: 0; top: 0; width: 100%; height: 18px; background: var(--brand); display: flex; justify-content: space-between; align-items: center; padding: 0 17px; }
  .top-bar .slide-title { font-family: "Ubuntu", sans-serif; font-weight: 500; font-size: 6.5px; letter-spacing: 0.4px; color: var(--white); }
  .top-bar .bar-name { font-family: "Ubuntu", sans-serif; font-weight: 500; font-size: 5.5px; color: var(--white); padding-right: 0; margin-right: -13px; }

  .ghost-name { position: absolute; left: 4px; bottom: -14px; font-family: "Ubuntu", sans-serif; font-weight: 700; font-size: 50px; letter-spacing: -0.5px; color: var(--ghost); white-space: nowrap; }

  /* Inset title bar */
  .title-bar { position: absolute; height: 18px; background: var(--brand); display: flex; align-items: center; padding-left: 8px; }
  .title-bar .slide-title { font-family: "Ubuntu", sans-serif; font-weight: 500; font-size: 6.5px; letter-spacing: 0.3px; color: var(--white); }
  .title-bar .pill { position: absolute; right: 27px; top: -1px; height: 20px; width: 44px; border-radius: 10px 0 0 10px; background: var(--white); display: flex; align-items: center; justify-content: center; font-family: "Ubuntu", sans-serif; font-weight: 500; font-size: 5px; color: var(--brand); white-space: nowrap; }

  .page-number { position: absolute; right: 14px; bottom: 9px; width: 7px; height: 7px; background: var(--brand); color: var(--white); font-size: 4px; line-height: 7px; text-align: center; }

  .copy { position: absolute; font-size: 4.3px; line-height: 8.2px; color: var(--copy-grey); }
  .copy p + p { margin-top: 0; }
  .copy strong { color: var(--brand); font-weight: 700; }
  .copy.is-brand { color: var(--brand); }
  .copy.is-brand strong { color: var(--brand); }

  .photo { position: absolute; left: 0; top: 0; width: 103px; height: 100%; }
  .photo.warm { background: linear-gradient(170deg, var(--photo-warm-1) 0%, #a08a6e 45%, var(--photo-warm-2) 100%); }
  .photo.cool { background: linear-gradient(170deg, var(--photo-cool-1) 0%, #2b3f7e 50%, var(--photo-cool-2) 100%); }
  .side-panel { position: absolute; left: 0; top: 0; width: 103px; height: 100%; background: var(--brand); }

  .chart { position: absolute; left: 218px; top: 70px; }

  .closing { background: var(--brand); }
  .closing-disc { position: absolute; left: 126px; top: 46px; width: 115px; height: 115px; border-radius: 50%; background: var(--white); display: flex; align-items: center; justify-content: center; }
  .closing-disc .name { font-family: "Ubuntu", sans-serif; font-weight: 500; font-size: 13px; color: var(--brand); }

  /* Spec strip */
  .spec-strip { position: absolute; left: 0; top: 734px; width: 1200px; height: 48px; background: var(--white); }
  .spec { position: absolute; font-size: 11px; color: #333; }
  .spec .label { color: var(--brand); }
  .spec-font { left: 413px; top: 18px; }
  .spec-colour-label { left: 662px; top: 18px; }
  .spec-colour-values { left: 707px; top: 10px; font-size: 10.5px; line-height: 14px; }
</style>
</head>
<body>

  <!-- Cover -->
  <section class="slide row-1 col-1 cover">
    <div class="cover-mark"><span class="dot"></span><span class="name">Vértice Lunar</span></div>
    <div class="cover-divider"></div>
    <h1 class="cover-title">TITLE GOES HERE</h1>
    <p class="cover-subtitle">ANOTHER SMALL TITLE</p>
    <div class="cover-footer"><span>AUTHOR : PRESENTER NAME</span><span>TITLE OR DETAILS GOES HERE</span></div>
  </section>

  <!-- Two-column text -->
  <section class="slide row-1 col-2">
    <div class="ghost-name">Vértice Lunar</div>
    <header class="top-bar"><span class="slide-title">TITLE OF THE SLIDE</span><span class="bar-name">Vértice Lunar</span></header>
    <div class="copy is-brand" style="left:17px; top:37px; width:161px;">
      <p>We give old buildings a second life. Our team studies each structure, keeps what still works and adapts the rest for new uses, from homes and offices to studios, shops and public spaces that serve the city for decades to come.</p>
      <p>Every project begins with a careful survey of walls, floors and roofs. We measure light, air and movement, then plan changes that respect the history of the place while meeting current rules for safety, comfort and energy use.</p>
      <p>Reuse saves materials, time and money. It keeps the character of a street alive and brings people back to quiet quarters, giving owners a clear path from first idea to opening day.</p>
      <p>Every project begins with a careful survey of walls, floors and roofs. We measure light, air and movement, then plan changes that respect the history of the place while meeting current rules for safety, comfort and energy use.</p>
    </div>
    <div class="copy" style="left:185px; top:37px; width:161px;">
      <p>Every project begins with a careful survey of walls, floors and roofs. We measure light, air and movement, then plan changes that respect the history of the place while meeting current rules for safety, comfort and energy use.</p>
      <p>We give old buildings a second life. Our team studies each structure, keeps what still works and adapts the rest for new uses, from homes and offices to studios, shops and public spaces that serve the city for decades to come. <strong style="color:#333">From study to site, we stay beside you.</strong></p>
      <p>Reuse saves materials, time and money. It keeps the character of a street alive and brings people back to quiet quarters, giving owners a clear path from first idea to opening day.</p>
      <p>We give old buildings a second life. Our team studies each structure, keeps what still works and adapts the rest for new uses, from homes and offices to studios, shops and public spaces that serve the city for decades to come.</p>
    </div>
    <span class="page-number">2</span>
  </section>

  <!-- Blank with header bar -->
  <section class="slide row-1 col-3">
    <div class="ghost-name">Vértice Lunar</div>
    <header class="top-bar"><span class="slide-title">TITLE OF THE SLIDE</span><span class="bar-name">Vértice Lunar</span></header>
    <span class="page-number">3</span>
  </section>

  <!-- Photo + text -->
  <section class="slide row-2 col-1">
    <div class="photo warm" role="img" aria-label="Photograph of an old stone tower above a cobbled street"></div>
    <div class="title-bar" style="left:114px; top:23px; width:244px;"><span class="slide-title">TITLE OF THE SLIDE</span><span class="pill">Vértice Lunar</span></div>
    <div class="copy" style="left:114px; top:57px; width:244px;">
      <p>We give old buildings a second life. Our team studies each structure, keeps what still works and adapts the rest for new uses, from homes and offices to studios, shops and public spaces that serve the city for decades to come. Every project begins with a careful survey of walls, floors and roofs. We measure light, air and movement, then plan changes that respect the history of the place while meeting current rules for safety, comfort and energy use. <strong>From study to site, we stay beside you.</strong></p>
      <p>Reuse saves materials, time and money. It keeps the character of a street alive and brings people back to quiet quarters, giving owners a clear path from first idea to opening day. Every project begins with a careful survey of walls, floors and roofs. We measure light, air and movement, then plan changes that respect the history of the place while meeting current rules for safety, comfort and energy use.</p>
      <p>We give old buildings a second life. Our team studies each structure, keeps what still works and adapts the rest for new uses, from homes and offices to studios, shops and public spaces that serve the city for decades to come. Reuse saves materials, time and money. It keeps the character of a street alive and brings people back to quiet quarters, giving owners a clear path from first idea to opening day.</p>
    </div>
    <span class="page-number">4</span>
  </section>

  <!-- Tinted photo + text -->
  <section class="slide row-2 col-2">
    <div class="photo cool" role="img" aria-label="Blue-tinted photograph of an old stone tower above a cobbled street"></div>
    <div class="title-bar" style="left:114px; top:23px; width:244px;"><span class="slide-title">TITLE OF THE SLIDE</span><span class="pill">Vértice Lunar</span></div>
    <div class="copy" style="left:114px; top:57px; width:244px;">
      <p>We give old buildings a second life. Our team studies each structure, keeps what still works and adapts the rest for new uses, from homes and offices to studios, shops and public spaces that serve the city for decades to come. Every project begins with a careful survey of walls, floors and roofs. We measure light, air and movement, then plan changes that respect the history of the place while meeting current rules for safety, comfort and energy use. <strong>From study to site, we stay beside you.</strong></p>
      <p>Reuse saves materials, time and money. It keeps the character of a street alive and brings people back to quiet quarters, giving owners a clear path from first idea to opening day. Every project begins with a careful survey of walls, floors and roofs. We measure light, air and movement, then plan changes that respect the history of the place while meeting current rules for safety, comfort and energy use.</p>
      <p>We give old buildings a second life. Our team studies each structure, keeps what still works and adapts the rest for new uses, from homes and offices to studios, shops and public spaces that serve the city for decades to come. Reuse saves materials, time and money. It keeps the character of a street alive and brings people back to quiet quarters, giving owners a clear path from first idea to opening day.</p>
    </div>
    <span class="page-number">5</span>
  </section>

  <!-- Side panel -->
  <section class="slide row-2 col-3">
    <div class="side-panel"></div>
    <div class="title-bar" style="left:114px; top:23px; width:244px;"><span class="slide-title">TITLE OF THE SLIDE</span><span class="pill">Vértice Lunar</span></div>
    <span class="page-number">6</span>
  </section>

  <!-- Text + chart -->
  <section class="slide row-3 col-1">
    <div class="title-bar" style="left:11px; top:10px; width:348px;"><span class="slide-title">TITLE OF THE SLIDE</span><span class="pill">Vértice Lunar</span></div>
    <div class="copy" style="left:27px; top:42px; width:141px;">
      <p>We give old buildings a second life. Our team studies each structure, keeps what still works and adapts the rest for new uses, from homes and offices to studios, shops and public spaces that serve the city for decades to come.</p>
      <p>Every project begins with a careful survey of walls, floors and roofs. We measure light, air and movement, then plan changes that respect the history of the place while meeting current rules for safety, comfort and energy use. <strong>From study to site, we stay beside you.</strong></p>
      <p>Reuse saves materials, time and money. It keeps the character of a street alive and brings people back to quiet quarters, giving owners a clear path from first idea to opening day.</p>
      <p>We give old buildings a second life. Our team studies each structure, keeps what still works and adapts the rest for new uses, from homes and offices to studios, shops and public spaces that serve the city for decades to come.</p>
    </div>
    <svg class="chart" width="110" height="72" viewBox="0 0 110 72" aria-label="Bar chart of growth from 2004 to 2011">
      <g>
        <path d="M4 56 V49 A4 4 0 0 1 12 49 V56 Z" fill="#E0484A"/>
        <path d="M17 56 V47 A4 4 0 0 1 25 47 V56 Z" fill="#F0803C"/>
        <path d="M30 56 V44 A4 4 0 0 1 38 44 V56 Z" fill="#F2A93B"/>
        <path d="M43 56 V41 A4 4 0 0 1 51 41 V56 Z" fill="#B6AD3A"/>
        <path d="M56 56 V36 A4 4 0 0 1 64 36 V56 Z" fill="#7FA852"/>
        <path d="M69 56 V30 A4 4 0 0 1 77 30 V56 Z" fill="#5FA08E"/>
        <path d="M82 56 V22 A4 4 0 0 1 90 22 V56 Z" fill="#7A9CB0"/>
        <path d="M95 56 V7 A4 4 0 0 1 103 7 V56 Z" fill="#6EC6F0"/>
      </g>
      <line x1="2" y1="56.5" x2="105" y2="56.5" stroke="#E2E2E2" stroke-width="0.5"/>
      <g>
        <circle cx="8" cy="61" r="1.2" fill="#E0484A"/>
        <circle cx="21" cy="61" r="1.2" fill="#F0803C"/>
        <circle cx="34" cy="61" r="1.2" fill="#F2A93B"/>
        <circle cx="47" cy="61" r="1.2" fill="#B6AD3A"/>
        <circle cx="60" cy="61" r="1.2" fill="#7FA852"/>
        <circle cx="73" cy="61" r="1.2" fill="#5FA08E"/>
        <circle cx="86" cy="61" r="1.2" fill="#7A9CB0"/>
        <circle cx="99" cy="61" r="1.2" fill="#6EC6F0"/>
      </g>
      <g font-family="Source Sans 3, sans-serif" font-size="3.2" fill="#A0A0A0" text-anchor="middle">
        <text x="8" y="67">2004</text><text x="21" y="67">2005</text><text x="34" y="67">2006</text><text x="47" y="67">2007</text>
        <text x="60" y="67">2008</text><text x="73" y="67">2009</text><text x="86" y="67">2010</text><text x="99" y="67">2011</text>
      </g>
    </svg>
    <span class="page-number">7</span>
  </section>

  <!-- Blank with inset bar -->
  <section class="slide row-3 col-2">
    <div class="title-bar" style="left:13px; top:10px; width:346px;"><span class="slide-title">TITLE OF THE SLIDE</span><span class="pill">Vértice Lunar</span></div>
    <span class="page-number">8</span>
  </section>

  <!-- Closing -->
  <section class="slide row-3 col-3 closing">
    <div class="closing-disc"><span class="name">Vértice Lunar</span></div>
  </section>

  <!-- Spec strip -->
  <footer class="spec-strip">
    <p class="spec spec-font"><span class="label">FONT :</span> SOURCE SANS PRO / + UBUNTU</p>
    <p class="spec spec-colour-label"><span class="label">COLOR :</span></p>
    <p class="spec spec-colour-values">Text #4364B0<br>Title #FFFFFF</p>
  </footer>

</body>
</html>
```